Business Card Needed for Crafter of Pottery, Jewelry and Artwork

Calling all designers in search of an artistic challenge.

I need a new business card design for my pottery, jewelry and artwork business, Woven Glass and Tide, based in Vancouver BC.

I would like a card that is bright and inviting and preferably incorporates my logo and a sample of photos of my work while having a clean fresh look. The following contact details would preferably be included on the card as well:
• Helena Pikeworth
• Designer
• Phone: 604.555.0172
• Email: Designer@WovenGlassandTide.example
• Website: www.WovenGlassandTide.example
• Blog: www.ShapingHillside.example

The logo is attached in two color schemes in both Vector and Source formats. On past cards I’ve also included photos of my work. By including photos of the work the pieces are showcased and it catches people’s eye and prompts them to pick up the card and look at it more closely. For example, if I leave a stack in a coffee shop I want people to be drawn to the card, to pick it up and get a sense of the my product lines. Please feel free to pull photos of my work directly off of my website. If you need photos with higher pixels please let me know and I’ll email them directly to you. The website background is bffbda (191, 251, 218). I would like the business cards to match the feel of the website for consistency but the cards do not need to use the exact same colors. My website and current business card are predominantly turquoise shades. The background uses stripes provided by the website template. I don’t know the exact colors of the stripes.

My current business card is attached to show the use of photos in a design. Please note that I am not thrilled with my own design and am looking for variations and completely new designs. This example is not meant to be used as a template or starting point.

Here is some background surrounding my company:
WGT offers one of a kind jewelry, pottery, artwork and leather bags each designed with a twist. The pottery varies from rustic every day functional ware to raku artwork. The jewelry ranges from simple sterling every day pieces to multimedia pieces incorporating stone, metal, ceramics and fabric. The artwork is multimedia, typically acrylic paired with a natural element such as bark. All the bags are leather with reworked kimono fabric or patterned silk lining.

Feel free to check out my website to get a flavour for my work and the color scheme I've used on marketing materials so far. www.wovenglassandtide.example
Updates

Thank you to everyone who has submitted a design so far. I hope everyone has received some helpful feedback.

I'm going to post a survey to customers and friends asking for their votes. If you have new designs to submit please try to get them in by Saturday March 30 at noon so that I can include it in the survey launch.

Thank you

Target Market(s)

Females aged 25-65 interested in one of a kind functional pottery and jewelry.

Industry/Entity Type

Coffee Shop

Requirements
Must have
• Contact information, website, blog
Nice to have
• Logo, photos

```html
<!DOCTYPE html>
<html lang="en">
<head>
<meta charset="utf-8">
<title>Woven Glass and Tide — Business Card</title>
<link rel="stylesheet" href="https://fonts.googleapis.com/css2?family=Source+Sans+3:wght@400;600&display=swap">
<style>
  :root {
    --teal: #56c8c0;
    --teal-light: #62d0c8;
    --navy: #22205a;
    --ink: #555a5e;
    --paper: #ffffff;
    --page: #ffffff;
    --font: "Source Sans 3", Arial, sans-serif;
  }
  html, body {
    margin: 0;
    width: 1200px;
    height: 1000px;
    overflow: hidden;
    background: var(--page);
    font-family: var(--font);
  }
  .canvas { position: relative; width: 1200px; height: 1000px; }

  .card {
    position: absolute;
    left: 274px;
    width: 654px;
    height: 374px;
    border-radius: 22px;
    overflow: hidden;
    background: var(--paper);
    box-shadow: 4px 6px 8px rgba(0,0,0,0.35);
  }
  .card--front { top: 94px; }
  .card--back { top: 533px; background: var(--teal); }

  .stripes {
    position: absolute; left: 0; top: 0; width: 100%;
    background: repeating-linear-gradient(90deg,
      var(--teal) 0 32px, var(--teal-light) 32px 64px);
  }
  .card--front .stripes { height: 120px; }
  .card--back .stripes { height: 110px; }

  .name-band {
    position: absolute; left: 0; top: 120px; width: 100%; height: 74px;
    background: var(--navy);
  }
  .accent-band {
    position: absolute; left: 0; top: 194px; width: 100%; height: 14px;
    background: var(--teal);
  }

  .brand-seal {
    position: absolute;
    border-radius: 50%;
    background: var(--paper);
    display: flex; align-items: center; justify-content: center;
    text-align: center;
    color: var(--navy);
    font-weight: 600;
    line-height: 1.1;
    box-sizing: border-box;
  }
  .card--front .brand-seal {
    left: 50px; top: 56px; width: 212px; height: 212px;
    border: 5px solid var(--teal);
    font-size: 26px; padding: 0 30px;
  }
  .card--back .brand-seal {
    left: 236px; top: 96px; width: 180px; height: 180px;
    border: 9px solid var(--navy);
    font-size: 22px; padding: 0 26px;
  }

  .person {
    position: absolute; right: 44px; top: 128px; text-align: right;
  }
  .person__name { color: var(--teal); font-size: 24px; font-weight: 600; line-height: 1.2; }
  .person__role { color: var(--paper); font-size: 18px; line-height: 1.25; }

  .contact {
    position: absolute; right: 36px; top: 234px;
    list-style: none; margin: 0; padding: 0;
    color: var(--ink); font-size: 18.5px;
  }
  .contact li {
    display: flex; align-items: center; justify-content: flex-end;
    height: 25.5px;
  }
  .contact svg { width: 18px; height: 18px; margin-left: 6px; flex: none; }

  .gallery-rule {
    position: absolute; left: 0; width: 100%; height: 11px; background: var(--navy);
  }
  .gallery-rule--top { top: 110px; }
  .gallery-rule--bottom { top: 253px; }

  .gallery {
    position: absolute; left: 0; top: 121px; width: 100%; height: 132px;
    display: flex; background: #ffffff;
  }
  .gallery__item { height: 100%; }
  .gallery__item--bowl { width: 149px; background: linear-gradient(135deg, #e6e3df, #8c7d72 55%, #3a2f2b); }
  .gallery__item--jar { width: 88px; background: radial-gradient(circle at 50% 60%, #3a5fb0, #26407e 55%, #d9dde3 90%); }
  .gallery__item--gap { width: 170px; background: #eef0f2; }
  .gallery__item--pendant { width: 117px; background: radial-gradient(circle at 50% 55%, #8fa0a6, #cfc8bb 45%, #bdb5a8); }
  .gallery__item--bag { flex: 1; background: linear-gradient(160deg, #f4f4f4, #2fb4bf 45%, #9aa0a3 80%, #f2f2f2); }

  .web-address {
    position: absolute; left: 0; width: 100%; top: 318px;
    text-align: center; color: var(--paper); font-size: 20px;
  }
</style>
</head>
<body>
<main class="canvas">

  <section class="card card--front" aria-label="Business card front">
    <div class="stripes"></div>
    <div class="name-band"></div>
    <div class="accent-band"></div>
    <div class="brand-seal">Woven Glass and Tide</div>

    <div class="person">
      <div class="person__name">Helena Pikeworth</div>
      <div class="person__role">Designer</div>
    </div>

    <ul class="contact">
      <li>604.555.0172
        <svg viewBox="0 0 20 20" aria-hidden="true"><path fill="#56c8c0" d="M2 7c0-3 3-4 8-4s8 1 8 4v1h-4V6H6v2H2zM5 9h10l2 8H3z"/><circle cx="10" cy="13" r="2" fill="#fff"/></svg>
      </li>
      <li>Designer@WovenGlassandTide.example
        <svg viewBox="0 0 20 20" aria-hidden="true"><rect x="1" y="4" width="18" height="12" fill="#56c8c0"/><path d="M1 4l9 7 9-7" fill="none" stroke="#fff" stroke-width="1.5"/></svg>
      </li>
      <li>www.WovenGlassandTide.example
        <svg viewBox="0 0 20 20" aria-hidden="true"><g fill="none" stroke="#56c8c0" stroke-width="1.5"><circle cx="10" cy="10" r="8"/><ellipse cx="10" cy="10" rx="3.5" ry="8"/><path d="M2 10h16M4 6h12M4 14h12"/></g></svg>
      </li>
      <li>www.ShapingHillside.example
        <svg viewBox="0 0 20 20" aria-hidden="true"><rect x="1" y="1" width="18" height="18" rx="4" fill="#56c8c0"/></svg>
      </li>
    </ul>
  </section>

  <section class="card card--back" aria-label="Business card back">
    <div class="stripes"></div>
    <div class="gallery-rule gallery-rule--top"></div>
    <div class="gallery">
      <div class="gallery__item gallery__item--bowl" role="img" aria-label="Photo of a glazed ceramic bowl"></div>
      <div class="gallery__item gallery__item--jar" role="img" aria-label="Photo of a speckled blue lidded jar"></div>
      <div class="gallery__item gallery__item--gap"></div>
      <div class="gallery__item gallery__item--pendant" role="img" aria-label="Photo of a pendant necklace on linen"></div>
      <div class="gallery__item gallery__item--bag" role="img" aria-label="Photo of a turquoise leather bag with silk lining"></div>
    </div>
    <div class="gallery-rule gallery-rule--bottom"></div>
    <div class="brand-seal">Woven Glass and Tide</div>
    <div class="web-address">www.WovenGlassandTide.example</div>
  </section>

</main>
</body>
</html>
```